Tri Herb seasoning blends, 9 variants- looking to freshen up label

Looking for new look for the USA and Australasia market.

Position of brand: Gluten Free & Low Salt seasoning blends.
67,000,000 - high blood pressure- Low salt - focus
2,000,000,000- gluten free

Needs: New Eye catching Label which screams the message of Low salt & gluten free, but tastes great. Take a look at my competitors. My "chef" image on front of label is my father - keep as is, but he can be freshened up take a look at his photo. You do not have to use the chef- its your design coice- I am open.

Each variant has a purpose - Coastal Tri Herb purpose is "use instead of salt & pepper' This is the only "purpose statement" we want to keep.

Shipping Package: Popup display - Again designed to scream message.

You will need to research our website www.coastaltriherb-example.com for information on product and ask as many question as you like.

Target Market(s)

Low salt healthy minded, gluten free

Industry/Entity Type

Shipping

Requirements
Must have
• Keep character as is - can be tweaked, freshen up. I have been building this brand based on this image for 7 years, it really just needs a modern, professional feel to it now.

Please pay attention to the look and feel of product above. How can we make a cartoon character on the front of the bottle look elegant?

But do not have to use the character at all.
Nice to have
• Health rating guide, if keeping character on front or maybe small one an back? Maybe have him hold a plate of real food...

Should not have
• bold color

```html
<!DOCTYPE html>
<html lang="en">
<head>
<meta charset="utf-8">
<title>Tri Herb Seasoning Labels</title>
<link rel="stylesheet" href="https://fonts.googleapis.com/css2?family=Amatic+SC:wght@700&family=Dancing+Script:wght@600&family=Special+Elite&family=Roboto:wght@400;500&display=swap">
<style>
  :root {
    --page-bg: #ffffff;
    --label-bg: #f1ebc9;
    --ink: #1f1a17;
    --badge-red: #c8252b;
    --badge-face: #ffffff;
    --cajun: #7cb23b;
    --cajun-text: #6f9a33;
    --bacon: #f4aa2a;
    --bacon-text: #d19a3d;
    --coastal: #a75ccc;
    --coastal-text: #7b4f8c;
    --weight-text: #ffffff;
  }
  * { box-sizing: border-box; margin: 0; padding: 0; }
  html, body {
    width: 1200px; height: 959px; overflow: hidden;
    background: var(--page-bg);
  }
  .lineup {
    position: relative; width: 1200px; height: 959px;
    display: flex; justify-content: center; align-items: center; gap: 52px;
  }
  .label {
    position: relative; width: 330px; height: 440px;
    background: var(--label-bg);
    box-shadow: 0 2px 10px rgba(0,0,0,0.12);
    overflow: hidden;
  }
  .label--cajun   { --accent: var(--cajun);   --accent-text: var(--cajun-text); }
  .label--bacon   { --accent: var(--bacon);   --accent-text: var(--bacon-text); }
  .label--coastal { --accent: var(--coastal); --accent-text: var(--coastal-text); }

  .chef-art {
    position: absolute; left: 55px; top: 18px; width: 200px; height: 140px;
    border-radius: 40px 40px 20px 20px;
    background: radial-gradient(ellipse at 40% 25%, var(--accent) 0 30%, transparent 31%),
                linear-gradient(180deg, rgba(0,0,0,0.04), rgba(0,0,0,0.10));
    opacity: 0.85;
  }
  .facts {
    position: absolute; left: 10px; top: 185px;
    display: flex; flex-direction: column; gap: 22px;
  }
  .fact {
    width: 46px; height: 42px; border-radius: 4px;
    background: var(--badge-face);
    border: 1.5px solid var(--ink);
    overflow: hidden; text-align: center;
    font-family: "Roboto", sans-serif; color: var(--ink);
  }
  .fact__name {
    display: block; background: var(--badge-red); color: #fff;
    font-size: 9px; line-height: 13px;
  }
  .fact__value { display: block; font-size: 21px; line-height: 27px; }

  .variant {
    position: absolute; left: 70px; top: 170px;
    font-family: "Amatic SC", sans-serif; font-weight: 700;
    font-size: 92px; line-height: 1; letter-spacing: 2px; color: var(--ink);
  }
  .brand {
    position: absolute; left: 80px; top: 262px;
    font-family: "Dancing Script", cursive; font-weight: 600;
    font-size: 36px; color: var(--ink);
  }
  .purpose {
    position: absolute; left: 74px; top: 332px; width: 250px;
    font-family: "Special Elite", monospace;
    font-size: 20px; line-height: 23px; letter-spacing: 0.5px;
    color: var(--accent-text); text-transform: uppercase;
  }
  .weight-band {
    position: absolute; left: 0; right: 0; top: 392px; height: 38px;
    background: linear-gradient(90deg, var(--accent) 0%, var(--accent) 75%, rgba(255,255,255,0.25) 100%);
    clip-path: polygon(0 18%, 30% 4%, 70% 10%, 100% 0, 100% 88%, 65% 100%, 30% 92%, 0 100%);
  }
  .weight {
    position: absolute; right: 48px; top: 398px;
    font-family: "Roboto", sans-serif; font-size: 20px; color: var(--weight-text);
  }
</style>
</head>
<body>
<main class="lineup">

  <section class="label label--cajun">
    <div class="chef-art" role="img" aria-label="Illustration of a smiling chef in a green chef's hat"></div>
    <ul class="facts" style="list-style:none">
      <li class="fact"><span class="fact__name">Calories</span><span class="fact__value">0%</span></li>
      <li class="fact"><span class="fact__name">Sodium</span><span class="fact__value">4%</span></li>
      <li class="fact"><span class="fact__name">Fat</span><span class="fact__value">0%</span></li>
    </ul>
    <h2 class="variant">Cajun</h2>
    <p class="brand">Tri Herb</p>
    <p class="purpose">Use instead of salt &amp; pepper!</p>
    <div class="weight-band"></div>
    <p class="weight">85g</p>
  </section>

  <section class="label label--bacon">
    <div class="chef-art" role="img" aria-label="Illustration of a smiling chef in an orange chef's hat"></div>
    <ul class="facts" style="list-style:none">
      <li class="fact"><span class="fact__name">Calories</span><span class="fact__value">0%</span></li>
      <li class="fact"><span class="fact__name">Sodium</span><span class="fact__value">4%</span></li>
      <li class="fact"><span class="fact__name">Fat</span><span class="fact__value">0%</span></li>
    </ul>
    <h2 class="variant">Bacon</h2>
    <p class="brand">Tri Herb</p>
    <p class="purpose">Use instead of salt &amp; pepper!</p>
    <div class="weight-band"></div>
    <p class="weight">85g</p>
  </section>

  <section class="label label--coastal">
    <div class="chef-art" role="img" aria-label="Illustration of a smiling chef in a purple chef's hat"></div>
    <ul class="facts" style="list-style:none">
      <li class="fact"><span class="fact__name">Calories</span><span class="fact__value">0%</span></li>
      <li class="fact"><span class="fact__name">Sodium</span><span class="fact__value">4%</span></li>
      <li class="fact"><span class="fact__name">Fat</span><span class="fact__value">0%</span></li>
    </ul>
    <h2 class="variant">Coastal</h2>
    <p class="brand">Tri Herb</p>
    <p class="purpose">Use instead of salt &amp; pepper!</p>
    <div class="weight-band"></div>
    <p class="weight">85g</p>
  </section>

</main>
</body>
</html>
```